Pool Website

Need a simple front page and one internal page for a pool construction website. Please read the Must Have section for info. We uploaded 2 logos, one with color and one black and white. The colors you use in the logo can be changed, we used Century Gothic for the typing under the logo.

Nice clean design. The main back behind the site can be any color but we want the content back ground to be white.

We want a scrolling photo gallery (it doesn't have to scroll in your sample just know that's what we are envisioning) on the front page and the menu, and maybe a couple of photos down below to be clicked on such as this http://www.delmarwaterworks.example/

The 2ndary page would still have a header and menu and some type of cool design. Could be similar to this http://www.delmarwaterworks.example/about-us/awards.html

Also some other designs they like are here http://www.tessaloop.example/14-examples-of-clean-modern-website-design-inspiration/ I realize not all of these could have a image scroller on the front page which is fine.

Please do not copy their site exactly though it must be different.

For now you can just use sample stock photography for your photos for the design but ultimately we will swap them out for our own photos so there will not be a need to purchase stock photography of pools.

Menus will include Home - About - Services - Gallery - Contact - Blog

The current site is http://www.hughwestmorepools.example/ we do not want it to look anything like this. It's way too dark and just not professional looking. We want this new site to look very slick and professional.

We also want a space for social networking logos etc.

I have also attached 2 zip files that contain photos that may be used in the design. You do not have to use them all but you are welcome to use a few. Most will be put in the photo gallery.

Colors: Blues, white, grays, black, etc.
Updates

Added several photos that can be used in the design. Obviously you do not have to use them all most will be in the photo gallery but you're welcome to use some for your design. 

Target Market(s)

People with money for residential pools or companies that want corporate pools. Are target location is Miami and California

Industry/Entity Type

Construction

Font styles to use
Serif
Sans Serif

Requirements
Must have
• Nice clean design. The main back behind the site can be any color but we want the content back ground to be white.

```html
<!DOCTYPE html>
<html lang="en">
<head>
<meta charset="utf-8">
<title>Hugh Westmore Pools</title>
<link href="https://fonts.googleapis.com/css2?family=Questrial&family=Montserrat:wght@600;700&display=swap" rel="stylesheet">
<style>
:root{
  --navy:#252a5e;
  --teal:#1db7c3;
  --ink:#1a1a2c;
  --footer:#15162b;
  --gray-text:#8b8c98;
  --light-gray:#e9e9ee;
  --band-gray:#e4e4e7;
  --white:#ffffff;
}
*{box-sizing:border-box;margin:0;padding:0}
html,body{width:779px;height:1200px;overflow:hidden}
body{position:relative;background:var(--white);font-family:"Questrial",sans-serif;color:var(--ink)}
.abs{position:absolute}

/* header */
.site-header{left:0;top:0;width:779px;height:90px;background:var(--white);border-top:4px solid #e6e6e8;box-shadow:0 2px 4px rgba(0,0,0,.08)}
.brand{left:86px;top:24px;display:flex;align-items:center;gap:8px}
.brand-mark{width:22px;height:22px;background:var(--navy);border-radius:3px}
.brand-name{font-family:"Montserrat",sans-serif;font-weight:700;font-size:9px;color:var(--navy);line-height:1.25;width:62px}
.tagline span{position:absolute;top:20px;font-size:9.5px;color:var(--navy);white-space:nowrap}
.tagline strong{font-family:"Montserrat",sans-serif;font-weight:700}
.tagline svg{position:absolute;left:586px;top:21px}
.main-nav a{position:absolute;top:51px;font-size:10px;letter-spacing:.6px;color:var(--navy);text-decoration:none;line-height:20px;white-space:nowrap}
.main-nav .active{background:var(--navy);color:var(--white);width:54px;text-align:center;border-radius:3px}

/* hero */
.hero{left:0;top:90px;width:779px;height:270px;background:linear-gradient(180deg,#dfe8ea 0%,#a9b98a 35%,#6d8a4e 50%,#2f86b8 62%,#1f6ea6 80%,#b8ad99 100%)}
.slider-bar{left:0;top:360px;width:779px;height:30px;background:var(--band-gray);box-shadow:0 2px 3px rgba(0,0,0,.08)}
.dots{left:375px;top:373px;display:flex;gap:4px}
.dots span{width:5px;height:5px;border-radius:50%;background:#b6b6bc}
.dots span.on{background:var(--navy)}
.social-top{left:598px;top:369px;display:flex;gap:24px}
.social-top span{width:10px;height:10px;background:#a3a3ab;border-radius:2px}

/* offer */
.offer{left:80px;top:416px;width:616px;height:44px;border:1px solid #dcdce2;background:#f6f6f8}
.offer-title{position:absolute;left:24px;top:12px;font-family:"Montserrat",sans-serif;font-weight:700;font-size:16px;color:var(--navy);white-space:nowrap}
.offer-text{position:absolute;left:171px;top:10px;font-size:18px;color:var(--navy);white-space:nowrap}
.btn-teal{background:var(--teal);color:var(--white);font-family:"Montserrat",sans-serif;font-weight:600;border-radius:2px;display:flex;align-items:center;justify-content:center}
.offer .btn-teal{position:absolute;left:485px;top:9px;width:108px;height:25px;font-size:8.5px}

/* features */
.feature{width:205px}
.feature h3{font-family:"Montserrat",sans-serif;font-weight:600;font-size:11.5px;color:var(--navy);line-height:1.25}
.feature p{margin-top:26px;width:196px;font-size:8.5px;line-height:1.5;color:var(--gray-text)}

/* projects */
.section-title{left:80px;top:615px;font-size:15px;font-weight:400;color:var(--ink)}
.view-all{left:651px;top:621px;width:46px;height:16px;background:#c9c9ce;color:var(--white);font-size:6px;letter-spacing:.5px;display:flex;align-items:center;justify-content:center}
.project{width:202px}
.project-photo{height:90px}
.project h4{margin-top:10px;font-family:"Montserrat",sans-serif;font-weight:700;font-size:9px;color:var(--navy)}
.project p{margin-top:2px;width:170px;font-size:9.5px;line-height:1.3;color:var(--gray-text)}
.view-btn{left:87px;top:36px;width:36px;height:17px;background:var(--ink);color:var(--white);font-size:7px;display:flex;align-items:center;justify-content:center;border-radius:2px}

/* contact band */
.contact-band{left:0;top:822px;width:779px;height:378px;background:linear-gradient(90deg,#12a6b3,var(--teal) 20%,var(--teal) 80%,#12a6b3)}
.contact-card{left:60px;top:837px;width:660px;height:111px;background:var(--white)}
.contact-card h2{position:absolute;left:22px;top:14px;font-family:"Montserrat",sans-serif;font-weight:700;font-size:12px;color:var(--ink)}
.contact-card .intro{position:absolute;left:22px;top:38px;width:180px;font-size:8.5px;line-height:1.4;color:var(--ink)}
.field-label{position:absolute;font-size:9px;color:var(--ink)}
.field{position:absolute;background:var(--light-gray)}
.contact-card .btn-teal{position:absolute;left:591px;top:89px;width:39px;height:19px;font-size:8px}

/* footer */
.footer{left:60px;top:958px;width:660px;height:184px;background:var(--footer)}
.footer h5{position:absolute;font-family:"Montserrat",sans-serif;font-weight:700;font-size:9.5px;color:var(--white);letter-spacing:.3px}
.address{position:absolute;left:22px;top:48px;font-size:9px;line-height:1.35;color:#8a8ba6}
.phone{position:absolute;left:22px;top:95px;font-size:12px;color:var(--white);display:flex;align-items:center;gap:10px}
.email{position:absolute;left:22px;top:116px;font-size:8px;color:var(--white);display:flex;align-items:center;gap:10px}
.social-foot{position:absolute;left:22px;top:141px;display:flex;gap:17px}
.social-foot span{width:11px;height:11px;background:var(--white);border-radius:2px}
.map{position:absolute;left:229px;top:48px;width:192px;height:120px;border:3px solid var(--white);background:linear-gradient(135deg,#e8e4d6,#d9e0c9 45%,#cfdbe4 70%,#ebe6da)}
.services{position:absolute;left:470px;top:46px;list-style:none;font-size:8.5px;color:#8a8ba6}
.services li{height:17.6px;display:flex;align-items:center}
.services li::before{content:"›";color:var(--teal);margin-right:12px;font-size:10px}
.legal{left:60px;top:1150px;width:660px;height:34px;background:var(--footer);font-size:7px;color:#7a7b96;display:flex;align-items:center;justify-content:space-between;padding:0 22px}
.legal span + span{margin-left:10px}
.to-top{left:732px;top:1158px}
</style>
</head>
<body>

<header class="site-header abs">
  <div class="brand abs"><span class="brand-mark"></span><span class="brand-name">HUGH WESTMORE POOLS</span></div>
  <div class="tagline">
    <span style="left:188px"><strong>FAMILY OWNED FOR OVER 30 YEARS!</strong></span>
    <span style="left:380px">Serving Broward, Palm &amp; Miami-Dade Counties</span>
    <svg width="11" height="9" viewBox="0 0 11 9"><path d="M1 8 C2 4 5 3 8 3 L8 1 L11 4 L8 7 L8 5 C5 5 3 6 1 8Z" fill="var(--teal)"/></svg>
    <span style="left:605px"><strong>CALL US</strong></span>
    <span style="left:651px">954-555-0148</span>
  </div>
  <nav class="main-nav">
    <a class="active" href="#" style="left:288px">HOME</a>
    <a href="#" style="left:384px">ABOUT</a>
    <a href="#" style="left:449px">SERVICES</a>
    <a href="#" style="left:528px">GALLERY</a>
    <a href="#" style="left:604px">BLOG</a>
    <a href="#" style="left:664px">CONTACT</a>
  </nav>
</header>

<div class="hero abs" role="img" aria-label="Backyard pool with a raised spa, palm trees and desert landscaping"></div>
<div class="slider-bar abs"></div>
<div class="dots abs"><span></span><span></span><span class="on"></span><span></span></div>
<div class="social-top abs"><span></span><span></span><span></span><span></span></div>

<section class="offer abs">
  <span class="offer-title">SPECIAL OFFER</span>
  <span class="offer-text">Free Estimates &amp; Design Consults</span>
  <span class="btn-teal">Contact Us Today</span>
</section>

<div class="feature abs" style="left:84px;top:499px">
  <h3>Family Owned<br>since 1979</h3>
  <p>Pellentesque habitant morbi tristique senectus et netus et malesuada fames ac turpis egestas. In elit lacus, pellentesque sed sollicitudin in,</p>
</div>
<div class="feature abs" style="left:292px;top:499px">
  <h3>Coastal Pool &amp; Spa<br>Guild Member</h3>
  <p>Pellentesque habitant morbi tristique senectus et netus et malesuada fames ac turpis egestas. In elit lacus, pellentesque sed sollicitudin in,</p>
</div>
<div class="feature abs" style="left:500px;top:499px">
  <h3>Awarded over 75<br>CPSG Awards</h3>
  <p>Pellentesque habitant morbi tristique senectus et netus et malesuada fames ac turpis egestas. In elit lacus, pellentesque sed sollicitudin in,</p>
</div>

<h2 class="section-title abs">Recent Projects</h2>
<div class="view-all abs">VIEW ALL</div>

<article class="project abs" style="left:80px;top:646px">
  <div class="project-photo" role="img" aria-label="Modern white house with a rectangular pool and spa" style="background:linear-gradient(180deg,#e9edef 0%,#9bb7a2 40%,#3fa9d6 65%,#d9dcdc 100%)"></div>
  <h4>Malesuada dignissim</h4>
  <p>Cras lacus eros, consectetur eget bibendum ac, malesuada vitae felis.</p>
</article>
<article class="project abs" style="left:288px;top:646px">
  <div class="project-photo" role="img" aria-label="Freeform pool with a round spa and stone deck" style="background:linear-gradient(180deg,#cdd6c4 0%,#8fa39a 30%,#2b7fa6 60%,#b49c7e 100%)"></div>
  <h4>Malesuada dignissim</h4>
  <p>Cras lacus eros, consectetur eget bibendum ac, malesuada vitae felis.</p>
</article>
<article class="project abs" style="left:496px;top:646px">
  <div class="project-photo" role="img" aria-label="Curved turquoise pool beside a sunny patio" style="background:linear-gradient(160deg,#4fc3e0 0%,#2fa8d4 45%,#9fd9e8 70%,#e2e3dc 100%)"></div>
  <div class="view-btn abs">View</div>
  <h4>Malesuada dignissim</h4>
  <p>Cras lacus eros, consectetur eget bibendum ac, malesuada vitae felis.</p>
</article>

<div class="contact-band abs"></div>

<section class="contact-card abs">
  <h2>Contact Us</h2>
  <p class="intro">Please fill out the form to your right. Cras lacus eros, consectetur eget bibendum ac, male suada vitae felis. Aenean posuere ipsum ut tellus consequat commodo.</p>
  <span class="field-label" style="left:233px;top:14px">Name</span>
  <span class="field" style="left:233px;top:29px;width:164px;height:22px"></span>
  <span class="field-label" style="left:233px;top:59px">Email</span>
  <span class="field" style="left:233px;top:73px;width:164px;height:22px"></span>
  <span class="field-label" style="left:438px;top:14px">Question / Message</span>
  <span class="field" style="left:438px;top:29px;width:193px;height:56px"></span>
  <span class="btn-teal">Send</span>
</section>

<footer class="footer abs">
  <h5 style="left:22px;top:20px">HUGH WESTMORE POOLS</h5>
  <p class="address">2270 NW 41 Court<br>Coral Harbor<br>FL 33099</p>
  <p class="phone"><svg width="9" height="9" viewBox="0 0 10 10"><path d="M2 0.5 L4 2.8 L3 4 C3.6 5.4 4.6 6.4 6 7 L7.2 6 L9.5 8 L8.3 9.5 C4.5 9.3 0.7 5.5 0.5 1.7Z" fill="var(--teal)"/></svg>954-555-0148</p>
  <p class="email"><svg width="9" height="7" viewBox="0 0 9 7"><rect width="9" height="7" fill="var(--teal)"/><path d="M0 0 L4.5 3.8 L9 0" stroke="var(--footer)" fill="none"/></svg>contact@hughwestmorepools.example</p>
  <div class="social-foot"><span></span><span></span><span></span><span></span></div>

  <h5 style="left:231px;top:20px">Visit Our SHOWROOM</h5>
  <div class="map" role="img" aria-label="Street map showing the showroom location"></div>

  <h5 style="left:465px;top:23px">Services</h5>
  <ul class="services">
    <li>Commercial Pool Installation</li>
    <li>Pool Maintenance</li>
    <li>Pool Remodeling</li>
    <li>Pool Renovation</li>
    <li>Swimming Pool Installation</li>
    <li>Pool Repair</li>
  </ul>
</footer>

<div class="legal abs">
  <span>© Copyright 2014 Hugh Westmore Pools. All Rights Reserved.</span>
  <span><span>Terms &amp; Conditions</span><span>Privacy Policy</span></span>
</div>
<svg class="to-top abs" width="22" height="14" viewBox="0 0 22 14"><path d="M2 12 L11 3 L20 12" stroke="var(--footer)" stroke-width="1.5" fill="none"/></svg>

</body>
</html>
```